New brand of Beef Tallow. Label & carton design for BBQ enthusiasts

We currently have a PET tub that will be clear, and a solid black lid. It will be 500gm in net weight and be used to store beef tallow. The brand will be under the Tarnby Jarworks Co brand, and this has an existing logo. We want the ultimate design to be informed by some niche brands that operate in the BBQ and condiments categories. I also need a carton design for the beef tallow- two colour max. ***Note that the label dieline is upside down!

Target Market(s)

BBQ Enthusiasts

Industry/Entity Type

Food, Consumer Goods

Requirements
Must have
• Tarnby Jarworks logo, all of the required labelling, Nutrition Information Panel (to be supplied), barcode, product attributes, a top of lid and wrap around label. Use of terminology such as 'Suet, Tallow, Beef Fat' which are the key indicators of the product. I also want it to reference that it is made in Papua New Guinea.

```html
<!DOCTYPE html>
<html lang="en">
<head>
<meta charset="utf-8">
<title>Tarnby Jarworks Co – Suet, Tallow, Beef Fat</title>
<link rel="stylesheet" href="https://fonts.googleapis.com/css2?family=Bebas+Neue&display=swap">
<style>
  :root {
    --page-bg: #f4f5f7;
    --label-black: #0c0c0c;
    --label-charcoal: #2b2b2b;
    --brand-orange: #ee8c17;
    --brand-orange-deep: #d8760f;
    --ink-dark: #111111;
    --title-white: #f2f2f2;
    --cow-brown: #7a5230;
    --cow-brown-dark: #4a2f1a;
  }
  * { box-sizing: border-box; margin: 0; padding: 0; }
  html, body {
    width: 1200px;
    height: 1200px;
    overflow: hidden;
    background: var(--page-bg);
  }
  .label {
    position: absolute;
    left: 240px;
    top: 245px;
    width: 720px;
    height: 711px;
    background: linear-gradient(90deg, var(--label-charcoal) 0%, var(--label-black) 20%, var(--label-black) 80%, var(--label-charcoal) 100%);
    overflow: hidden;
    font-family: "Bebas Neue", sans-serif;
  }
  .brand-banner {
    position: absolute;
    left: 193px;
    top: 0;
    width: 365px;
    height: 350px;
  }
  .brand-banner svg { display: block; }
  .brand-name {
    position: absolute;
    left: 0;
    top: 186px;
    width: 365px;
    text-align: center;
    color: var(--ink-dark);
    font-size: 44px;
    line-height: 1;
    letter-spacing: 1px;
  }
  .cow-illustration {
    position: absolute;
    left: 193px;
    top: 374px;
    width: 346px;
    height: 240px;
    border-radius: 40px 60px 30px 30px;
    background: radial-gradient(ellipse at 45% 40%, var(--cow-brown) 0%, var(--cow-brown-dark) 60%, rgba(74,47,26,0) 100%);
    opacity: 0.8;
  }
  .product-title {
    position: absolute;
    left: 0;
    top: 416px;
    width: 720px;
    text-align: center;
    color: var(--title-white);
    font-size: 71px;
    font-weight: 400;
    line-height: 0.97;
    letter-spacing: 1px;
  }
  .origin-badge {
    position: absolute;
    left: 379px;
    top: 570px;
    width: 104px;
    height: 106px;
  }
  .origin-badge svg { position: absolute; inset: 0; }
  .origin-text {
    position: absolute;
    inset: 0;
    text-align: center;
    color: var(--ink-dark);
    line-height: 1;
  }
  .origin-text .country-main { display: block; margin-top: 12px; font-size: 36px; }
  .origin-text .country-sub { display: block; margin-top: 8px; font-size: 17px; letter-spacing: 1px; }
  .net-volume {
    position: absolute;
    left: 249px;
    top: 644px;
    color: var(--brand-orange);
    font-size: 36px;
    line-height: 1;
  }
</style>
</head>
<body>
  <main class="label">
    <div class="brand-banner">
      <svg width="365" height="350" viewBox="0 0 365 350" aria-hidden="true">
        <defs>
          <linearGradient id="bannerFill" x1="0" y1="0" x2="0" y2="1">
            <stop offset="0" stop-color="#dd7a10"/>
            <stop offset="1" stop-color="#f09a22"/>
          </linearGradient>
        </defs>
        <path d="M0 0 H365 V293 Q182 396 0 293 Z" fill="url(#bannerFill)"/>
      </svg>
      <div class="brand-name">Tarnby Jarworks Co</div>
    </div>

    <div class="cow-illustration" role="img" aria-label="Engraved-style illustration of a standing cow in brown tones"></div>

    <h1 class="product-title">Suet, Tallow,<br>Beef Fat</h1>

    <div class="origin-badge">
      <svg width="104" height="106" viewBox="0 0 104 106" aria-hidden="true">
        <path d="M10 0 H94 Q104 0 104 10 V52 Q104 106 52 106 Q0 106 0 52 V10 Q0 0 10 0 Z" fill="var(--brand-orange)"/>
      </svg>
      <div class="origin-text">
        <span class="country-main">Papua</span>
        <span class="country-sub">New Guinea</span>
      </div>
    </div>

    <div class="net-volume">20L</div>
  </main>
</body>
</html>
```